Liquor Label / Aguardiente

Label design for liquor bottle. Designers may submit multiple submissions.

Product Description:
Name: Viento de Plata™
Alcohol Category: Aguardiente (which in Spanish most closely translates to “burning water”) – aguardiente is derived from
cane sugar and is a general term for a type of alcoholic spirit in many Central and South America countries.
Taste: A smooth liquor with a comfortable yet spicy finish
Smell: Subtle aroma of spicy jalapeños
Liquid Color: Clear
Bottle Color: Clear
See link for reference - http://www.kelvostamp.com/sites/default/files/styles/uc_product_full/public/Pemrow_0.jpg?itok=9QmT2xLp
Closure: Bar top / cork
Bottle Shape/Size: height = 8.67in; diameter of base = 3.70in; diameter of neck = 0.85in

Label may consist of two separate parts (i.e. front and back, front and vertical side), or one continuous label.

Designer has complete freedom with color, font etc. unless otherwise stated below. The label MUST
contain (but is not limited only to) the following text exactly as written in quotes below:
- “Viento de Plata”
- “Aguardiente”
- “Cane Neutral Spirit with Natural Flavors”
- “35% Alc./Vol.”
- “750 ml”
- “Bottled by WP Spirits, LLC” and “Nashville, TN” - “Government Warning: (1) According to the Surgeon General, women should not drink alcoholic beverages during
pregnancy because of the risk of birth defects. (2) Consumption of alcoholic beverages impairs your ability to
drive a car or operate machinery, and may cause health problems.” (text in previous quotes must be in all
capitalized letters, text must be 2 MM in height and quote must be separated 2MM by all other text)
- Must be dedicated empty space for bar code (approximately 0.75in. height x 1.25in. length)

Target Market(s)

Label should have mass market appeal.
Age: 21 – 28 years old (primary target market is 21+ year old college students and recent graduates)
Target Market Gender: Both male and female, with emphasis on male
Consumption Focus: Spirit will be consumed typically as a shot, primarily at bars and secondarily off premise (label design will be critical for making our product highly visible behind a bar)
Marketing Theme: South American elements. The official Viento de Plata mascot is a llama and the incorporation and use of a llama somewhere (however large or small) on the bottle is encourage but by no means required.

Industry/Entity Type

Health

Requirements
Should not have
• Elements that may lead a potential consumer to believe the beverage is a craft liquor or an artisan brand. Please do not include images of peppers.

```html
<!DOCTYPE html>
<html lang="en">
<head>
<meta charset="utf-8">
<title>Viento de Plata – Aguardiente Label</title>
<link rel="stylesheet" href="https://fonts.googleapis.com/css2?family=Arimo:wght@400;700&family=Cinzel:wght@600&family=Marck+Script&display=swap">
<style>
  :root {
    --paper: #ffffff;
    --ink: #111111;
    --wine-light: #7c1c1f;
    --wine-mid: #531115;
    --wine-dark: #2e070b;
    --gold: #d9b24c;
    --gold-light: #f6e39a;
    --gold-dark: #9c7424;
    --band-ink: #1b1308;
    --emblem-dark: #1d1a1a;
    --label-text: #ffffff;
  }
  * { box-sizing: border-box; margin: 0; padding: 0; }
  html, body { width: 1200px; height: 847px; overflow: hidden; background: var(--paper); }
  .canvas { position: relative; width: 1200px; height: 847px; font-family: "Arimo", Arial, sans-serif; color: var(--ink); }

  .label { position: absolute; width: 330px; height: 356px; overflow: hidden; }
  .label__pattern { position: absolute; inset: 0; background: radial-gradient(ellipse at 50% 45%, var(--wine-light) 0%, var(--wine-mid) 50%, var(--wine-dark) 100%); }

  .label--front { left: 451px; top: 42px; }
  .label--back { left: 818px; top: 42px; }
  .label--applied { left: 152px; top: 373px; transform: scale(0.727, 0.79); transform-origin: 0 0; }

  .brand-mark { position: absolute; left: 0; right: 0; display: flex; flex-direction: column; align-items: center; }
  .brand-mark__dot { border-radius: 50%; background: var(--emblem-dark); border: 4px solid var(--gold); }
  .brand-mark__name { font-family: "Cinzel", Georgia, serif; font-weight: 600; color: var(--gold); letter-spacing: 0.5px; white-space: nowrap; }

  .label--front-face .brand-mark { top: 70px; }
  .label--front-face .brand-mark__dot { width: 70px; height: 70px; }
  .label--front-face .brand-mark__name { font-size: 25px; margin-top: 30px; }

  .product-name { position: absolute; left: 0; right: 0; top: 234px; text-align: center; font-family: "Marck Script", cursive; font-size: 31px; color: var(--label-text); }

  .bottler-band { position: absolute; left: 0; right: 0; top: 286px; height: 47px; background: linear-gradient(90deg, var(--gold-dark), var(--gold-light) 30%, var(--gold) 60%, var(--gold-dark)); padding: 0 18px 8px 28px; display: flex; justify-content: space-between; align-items: flex-end; }
  .bottler-band__who { font-size: 13px; line-height: 16px; color: var(--band-ink); }
  .bottler-band__who strong { display: block; font-weight: 700; }
  .bottler-band__abv { font-size: 14px; color: var(--band-ink); }

  .label--back .brand-mark { top: 22px; }
  .label--back .brand-mark__dot { width: 38px; height: 38px; border-width: 3px; }
  .label--back .brand-mark__name { font-size: 13px; margin-top: 8px; }

  .spirit-facts { position: absolute; left: 16px; right: 16px; top: 92px; text-align: center; font-size: 9px; line-height: 13px; color: var(--gold-light); letter-spacing: 0.3px; }

  .divider { position: absolute; left: 62px; right: 62px; height: 2px; background: linear-gradient(90deg, transparent, var(--gold), transparent); }
  .divider::after { content: ""; position: absolute; left: 50%; top: -3px; width: 8px; height: 8px; margin-left: -4px; border-radius: 50%; background: var(--gold); }
  .divider--top { top: 130px; }
  .divider--bottom { top: 246px; }

  .warning { position: absolute; left: 18px; right: 18px; top: 139px; color: var(--label-text); font-size: 8.5px; line-height: 11px; text-align: center; text-transform: uppercase; }
  .warning ol { list-style: none; }
  .warning li { padding-left: 16px; text-indent: -16px; }

  .barcode-space { position: absolute; left: 30px; top: 268px; width: 100px; height: 60px; background: var(--paper); }
  .volume { position: absolute; left: 207px; top: 278px; color: var(--label-text); font-size: 15px; }
  .volume strong { font-size: 25px; font-weight: 700; }
  .price { position: absolute; left: 207px; top: 315px; color: var(--label-text); font-size: 15px; }

  .caption { position: absolute; top: 405px; font-size: 22px; color: var(--ink); }
  .caption--front { left: 445px; }
  .caption--back { left: 818px; }

  .script-wordmark { position: absolute; left: 518px; top: 632px; font-family: "Marck Script", cursive; font-size: 58px; color: var(--ink); }

  .standalone-mark { position: absolute; left: 850px; top: 668px; width: 300px; display: flex; align-items: center; justify-content: center; gap: 12px; }
  .standalone-mark__dot { width: 34px; height: 34px; border-radius: 50%; background: var(--gold); }
  .standalone-mark__name { font-family: "Cinzel", Georgia, serif; font-weight: 600; font-size: 24px; color: var(--gold-dark); white-space: nowrap; }
</style>
</head>
<body>
<main class="canvas">

  <section class="label label--front-face label--applied" aria-label="Front label as applied">
    <div class="label__pattern" role="img" aria-label="Dark red paisley background pattern"></div>
    <div class="brand-mark"><span class="brand-mark__dot"></span><span class="brand-mark__name">VIENTO DE PLATA™</span></div>
    <p class="product-name">Aguardiente</p>
    <div class="bottler-band">
      <p class="bottler-band__who"><strong>BOTTLED BY</strong>WP SPIRITS</p>
      <p class="bottler-band__abv">35% Alc./Vol.</p>
    </div>
  </section>

  <section class="label label--front-face label--front" aria-label="Front label">
    <div class="label__pattern" role="img" aria-label="Dark red paisley background pattern"></div>
    <div class="brand-mark"><span class="brand-mark__dot"></span><span class="brand-mark__name">VIENTO DE PLATA™</span></div>
    <p class="product-name">Aguardiente</p>
    <div class="bottler-band">
      <p class="bottler-band__who"><strong>BOTTLED BY</strong>WP SPIRITS</p>
      <p class="bottler-band__abv">35% Alc./Vol.</p>
    </div>
  </section>
  <p class="caption caption--front">FRONT</p>

  <section class="label label--back" aria-label="Back label">
    <div class="label__pattern" role="img" aria-label="Dark red paisley background pattern"></div>
    <div class="brand-mark"><span class="brand-mark__dot"></span><span class="brand-mark__name">VIENTO DE PLATA™</span></div>
    <div class="spirit-facts">
      <p>CANE NEUTRAL SPIRIT WITH NATURAL FLAVORS</p>
      <p>BOTTLED BY WP SPIRITS, LLC &middot; NASHVILLE, TN</p>
    </div>
    <div class="divider divider--top"></div>
    <div class="warning">
      <p>Government Warning:</p>
      <ol>
        <li>(1)&nbsp; According to the Surgeon General, women should not drink alcoholic beverages during pregnancy because of the risk of birth defects.</li>
        <li>(2)&nbsp; Consumption of alcoholic beverages impairs your ability to drive a car or operate machinery, and may cause health problems.</li>
      </ol>
    </div>
    <div class="divider divider--bottom"></div>
    <div class="barcode-space" aria-hidden="true"></div>
    <p class="volume"><strong>750</strong> ml</p>
    <p class="price">PRISE: 00000</p>
  </section>
  <p class="caption caption--back">BACK</p>

  <p class="script-wordmark">Aguardiente</p>

  <div class="standalone-mark">
    <span class="standalone-mark__dot"></span>
    <span class="standalone-mark__name">VIENTO DE PLATA™</span>
  </div>

</main>
</body>
</html>
```